Velmar Ops Business Cards

We need to design some upbeat business cards. We are an Industrial Rope Access Company/Height Safety Company that specialize in Rope Access, Confined Space, Anchor Points, Safety Systems, PPE Inspecions and Rigging.
Company name is Velmar Ops Ltd
Card is for Gareth Lomas the Company Director
His mobile number is 027 418 9072 and email is gareth@velmarops.co.nz. Website address is www.velmarops.co.nz.
We will post some pictures below to ensure you get a good idea of what we do.

```html
<!DOCTYPE html>
<html lang="en">
<head>
<meta charset="utf-8">
<title>Velmar Ops – Business Card</title>
<link rel="stylesheet" href="https://fonts.googleapis.com/css2?family=Exo+2:wght@600;700&family=Mulish:wght@400;500&display=swap">
<style>
  :root {
    --page-bg: #d8d3cb;
    --card-top: #f4f5f5;
    --card-bottom: #e6e8e9;
    --brand-blue: #1c5d8c;
    --name-blue: #1f5a84;
    --text-dark: #2c3942;
    --band-blue-dark: #0f2f5a;
    --band-blue-light: #1d4f86;
    --band-grey: #4a4f55;
    --tagline: #c9d3dd;
  }
  * { margin: 0; padding: 0; box-sizing: border-box; }
  html, body {
    width: 1200px;
    height: 1054px;
    overflow: hidden;
    background: var(--page-bg);
  }
  .card {
    position: absolute;
    left: 100px;
    top: 225px;
    width: 1000px;
    height: 604px;
    border-radius: 22px;
    overflow: hidden;
    background: linear-gradient(180deg, var(--card-top), var(--card-bottom));
    box-shadow: 0 10px 30px rgba(0,0,0,0.12);
  }
  .brand-name {
    position: absolute;
    left: 76px;
    top: 262px;
    font-family: "Exo 2", sans-serif;
    font-weight: 700;
    font-size: 66px;
    line-height: 1;
    color: var(--brand-blue);
    letter-spacing: 0.5px;
  }
  .person {
    position: absolute;
    left: 594px;
    top: 188px;
  }
  .person-name {
    font-family: "Exo 2", sans-serif;
    font-weight: 700;
    font-size: 44px;
    line-height: 1;
    color: var(--name-blue);
  }
  .person-role {
    margin-top: 14px;
    font-family: "Mulish", sans-serif;
    font-size: 24px;
    color: var(--text-dark);
  }
  .contacts {
    position: absolute;
    left: 594px;
    top: 318px;
    list-style: none;
    font-family: "Mulish", sans-serif;
    font-size: 25px;
    color: var(--text-dark);
  }
  .contacts li {
    display: flex;
    align-items: center;
    height: 38px;
  }
  .contacts svg {
    width: 20px;
    height: 20px;
    margin-right: 28px;
    fill: var(--name-blue);
  }
  .band {
    position: absolute;
    left: 0;
    bottom: 0;
    width: 1000px;
    height: 74px;
  }
  .tagline {
    position: absolute;
    left: 518px;
    bottom: 22px;
    font-family: "Mulish", sans-serif;
    font-size: 24px;
    color: var(--tagline);
    word-spacing: 2px;
    white-space: nowrap;
  }
  .tagline .sep { margin: 0 8px; }
</style>
</head>
<body>
  <div class="card">
    <div class="brand-name">Velmar Ops</div>

    <div class="person">
      <div class="person-name">Gareth Lomas</div>
      <div class="person-role">Director</div>
    </div>

    <ul class="contacts">
      <li>
        <svg viewBox="0 0 20 20" aria-hidden="true"><path d="M2 6c0-2 3-4 8-4s8 2 8 4v2h-4V6.5c-1-.6-2.4-1-4-1s-3 .4-4 1V8H2zM5 9h10l2 7H3z"/></svg>
        027 418 9072
      </li>
      <li>
        <svg viewBox="0 0 20 20" aria-hidden="true"><path d="M1 4h18v12H1zm2 1.5 7 5.5 7-5.5z"/></svg>
        gareth@velmarops.co.nz
      </li>
      <li>
        <svg viewBox="0 0 20 20" aria-hidden="true"><circle cx="10" cy="10" r="8"/><path d="M2 10h16M10 2c-3 3-3 13 0 16M10 2c3 3 3 13 0 16" stroke="#e9ebec" stroke-width="1.2" fill="none"/></svg>
        www.velmarops.co.nz
      </li>
    </ul>

    <svg class="band" viewBox="0 0 1000 74" aria-hidden="true">
      <defs>
        <linearGradient id="bandBlue" x1="0" y1="0" x2="1" y2="0">
          <stop offset="0" stop-color="#1d4f86"/>
          <stop offset="0.5" stop-color="#123a68"/>
          <stop offset="1" stop-color="#0f2f5a"/>
        </linearGradient>
      </defs>
      <rect x="0" y="52" width="430" height="22" fill="var(--band-grey)"/>
      <path d="M457 0H1000V74H423z" fill="url(#bandBlue)"/>
    </svg>

    <div class="tagline">Safety<span class="sep">|</span>Compliant<span class="sep">|</span>Satisfaction</div>
  </div>
</body>
</html>
```